Restaurant service company needs a website!

I am looking for a skilled web designer/developer to create a professional, responsive, and easy-to-navigate website for my company, which specializes in servicing restaurant cooking equipment. The site should communicate trust, reliability, and technical expertise to our target audience, restaurant owners, managers, and commercial kitchen operators. I have included the company logos, if any other format for them is needed please let me know.

Target Market(s)

restaurant owners, managers, and commercial kitchen operators

Industry/Entity Type

Commercial Kitchen Equipment Service

Coding

Coded - Design and coding required

Number of Pages Required

1 page

Font styles to use
Serif
Sans Serif

Requirements
Must have
• Contact and service request forms, Click-to-call functionality for mobile, Clean, modern layout with strong visuals, Easy navigation, mobile-friendly
Nice to have
• Testimonials or Reviews, If possible a click-to-text functionality for mobile.
Should not have
• Any mention of Refrigeration or HVAC, "Free Quotes"

```html
<!DOCTYPE html>
<html lang="en">
<head>
<meta charset="utf-8">
<title>Keystone Kitchen Service — Commercial Kitchen Equipment Service</title>
<link href="https://fonts.googleapis.com/css2?family=Playfair+Display:wght@600;700&family=Inter:wght@400;500;600&display=swap" rel="stylesheet">
<style>
:root{
  --navy:#1c2636;
  --navy-card:#2a3547;
  --navy-line:#3b475a;
  --teal:#1f8b8a;
  --teal-dark:#17706f;
  --ink:#1b2230;
  --muted:#5b6473;
  --line:#e3e7ec;
  --soft:#f4f6f8;
  --white:#ffffff;
  --star:#1f8b8a;
}
*{box-sizing:border-box;margin:0;padding:0}
html,body{width:1200px;height:4432px;overflow:hidden}
body{font-family:"Inter",Arial,sans-serif;color:var(--ink);background:var(--white);position:relative}
h1,h2,h3{font-family:"Playfair Display",Georgia,serif}
.btn{display:inline-flex;align-items:center;justify-content:center;gap:10px;border-radius:6px;font-weight:600;font-size:17px;height:48px;padding:0 26px;text-decoration:none;white-space:nowrap}
.btn-teal{background:var(--teal);color:var(--white)}
.btn-white{background:var(--white);color:var(--teal)}
.btn-outline{border:2px solid var(--teal);color:var(--teal);background:var(--white)}
.icon{width:20px;height:20px;fill:none;stroke:currentColor;stroke-width:2;stroke-linecap:round;stroke-linejoin:round;flex:none}

/* nav + hero */
.hero{position:absolute;top:0;left:0;width:1200px;height:512px;background:linear-gradient(100deg,#2a2f36 0%,#4a4f55 45%,#8a8c8d 75%,#5e6265 100%);overflow:hidden}
.hero-photo{position:absolute;inset:0}
.hero-photo::after{content:"";position:absolute;inset:0;background:linear-gradient(90deg,rgba(20,26,36,.75),rgba(20,26,36,.35))}
.nav{position:absolute;top:0;left:0;right:0;height:52px;background:var(--white);z-index:2;display:flex;align-items:center;justify-content:center;gap:40px;font-size:16px;font-weight:500}
.nav .call{position:absolute;right:16px;height:36px;font-size:15px;padding:0 16px}
.hero-copy{position:absolute;left:18px;top:120px;width:1100px;z-index:2;color:var(--white)}
.hero-copy h1{font-size:60px;line-height:1.0}
.hero-copy p{font-size:22px;line-height:1.4;margin-top:16px;width:1080px}
.hero-actions{position:absolute;left:18px;top:396px;z-index:2;display:flex;gap:20px}
.hero-actions .btn{height:42px}
.hero-actions .blank{width:210px;background:var(--white)}

/* services */
.services{position:absolute;top:512px;left:0;width:1200px;height:948px;background:var(--navy);color:var(--white);text-align:center}
.services h2{font-size:40px;margin-top:148px}
.services .lead{width:640px;margin:18px auto 0;font-size:17px;line-height:1.5;color:#d5dbe4}
.svc-cards{display:flex;gap:28px;margin:60px 16px 0}
.svc-card{flex:1;height:150px;background:var(--navy-card);border:1px solid var(--navy-line);border-radius:8px;padding:22px 26px}
.svc-card .badge{width:48px;height:48px;border-radius:50%;background:var(--teal);display:flex;align-items:center;justify-content:center;margin:0 auto 14px}
.svc-card h3{font-family:"Inter",sans-serif;font-size:17px;font-weight:600}
.svc-card p{font-size:13px;line-height:1.45;color:#c9d0da;margin-top:8px}
.equip{margin:64px 16px 0;height:240px;background:var(--navy-card);border:1px solid var(--navy-line);border-radius:8px;padding:28px 40px}
.equip h3{font-size:22px}
.equip ul{list-style:none;display:grid;grid-template-columns:repeat(4,1fr);row-gap:48px;margin-top:40px;font-size:15px;color:#dfe4eb}

/* trust */
.trust{position:absolute;top:1520px;left:0;width:1200px;height:660px}
.trust-copy{position:absolute;left:18px;top:36px;width:520px}
.trust-copy h2{font-size:38px;line-height:1.15}
.trust-copy p{font-size:16px;line-height:1.55;color:var(--muted);margin-top:18px}
.checks{list-style:none;margin-top:22px}
.checks li{display:flex;align-items:center;gap:12px;font-size:16px;font-weight:500;height:34px}
.checks .icon{color:var(--teal)}
.trust-actions{display:flex;gap:14px;margin-top:24px}
.trust-actions .btn{height:42px;font-size:15px}
.trust-photo{position:absolute;left:622px;top:32px;width:564px;height:410px;border-radius:10px;background:linear-gradient(160deg,#7b8790 0%,#3f4a55 45%,#1f2833 100%)}
.stats{position:absolute;left:622px;top:442px;width:564px;height:110px;background:var(--white);border:1px solid var(--line);border-radius:0 0 10px 10px;display:flex}
.stat{flex:1;text-align:center;padding-top:14px}
.stat + .stat{border-left:1px solid var(--line)}
.stat .icon{color:var(--teal);width:28px;height:28px}
.stat strong{display:block;font-size:26px;font-weight:700}
.stat span{font-size:13px;color:var(--muted)}

/* testimonials */
.reviews{position:absolute;top:2220px;left:0;width:1200px;height:790px;text-align:center}
.reviews h2{font-size:40px;margin-top:36px}
.reviews .lead{width:600px;margin:10px auto 0;font-size:18px;line-height:1.45;color:var(--muted)}
.quotes{display:flex;gap:24px;margin:52px 16px 0;text-align:left}
.quote{flex:1;height:330px;background:var(--white);border:1px solid var(--line);border-radius:8px;box-shadow:0 4px 14px rgba(20,30,50,.08);padding:22px 20px;position:relative}
.quote:nth-child(odd){transform:rotate(-1.5deg)}
.quote:nth-child(even){transform:rotate(1.5deg)}
.stars{color:var(--star);font-size:18px;letter-spacing:2px}
.quote p{font-size:13px;line-height:1.5;color:var(--muted);margin-top:12px;font-style:italic}
.quote .who{position:absolute;left:20px;bottom:24px;font-size:13px}
.quote .who strong{display:block;font-size:14px}
.quote .who span{color:var(--teal)}
.join{width:800px;height:200px;margin:40px auto 0;background:var(--soft);border:1px solid var(--line);border-radius:8px;padding-top:30px}
.join h3{font-size:24px}
.join p{font-size:15px;color:var(--muted);margin-top:10px}
.join .row{display:flex;gap:16px;justify-content:center;margin-top:22px}
.join .btn{height:42px;font-size:15px}

/* emergency */
.emergency{position:absolute;top:3032px;left:0;width:1200px;height:320px;background:var(--teal);color:var(--white);text-align:center}
.emergency h2{font-size:40px;margin-top:60px}
.emergency p{width:700px;margin:16px auto 0;font-size:19px;line-height:1.45}
.emergency .row{display:flex;gap:20px;justify-content:center;margin-top:30px}
.emergency .btn{height:44px;width:250px;font-size:16px;padding:0 16px}

/* request */
.request{position:absolute;top:3352px;left:0;width:1200px;height:728px;text-align:center}
.request h2{font-size:40px;margin-top:44px}
.request .lead{width:600px;margin:12px auto 0;font-size:19px;line-height:1.4;color:var(--muted)}
.form-card{position:absolute;left:80px;top:188px;width:500px;height:468px;background:var(--white);border:1px solid var(--line);border-radius:8px;box-shadow:0 4px 14px rgba(20,30,50,.06);padding:24px;text-align:left}
.form-card h3{font-size:24px;padding-bottom:14px;border-bottom:1px solid var(--line)}
.grid{display:grid;grid-template-columns:1fr 1fr;gap:14px 20px;margin-top:16px}
.field label{display:block;font-size:12px;font-weight:600;margin-bottom:6px}
.field .input{height:32px;border:1px solid var(--line);border-radius:4px;font-size:12px;color:#9aa2ad;padding:8px 10px}
.field.full{grid-column:1/3}
.field .area{height:84px}
.form-card .btn{width:100%;height:34px;font-size:14px;margin-top:18px}
.contact-card{position:absolute;left:620px;top:188px;width:500px;height:220px;background:var(--white);border:1px solid var(--line);border-radius:8px;padding:24px;text-align:left}
.contact-card h3{font-size:24px;padding-bottom:14px;border-bottom:1px solid var(--line)}
.c-row{display:flex;gap:14px;margin-top:18px;font-size:13px}
.c-row .dot{width:34px;height:34px;border-radius:50%;background:#e2f1f1;color:var(--teal);display:flex;align-items:center;justify-content:center;flex:none}
.c-row strong{display:block}
.c-row span{color:var(--teal)}
.alert-card{position:absolute;left:620px;top:420px;width:500px;height:180px;background:var(--teal);color:var(--white);border-radius:8px;padding:22px;text-align:left}
.alert-card h3{font-family:"Inter",sans-serif;font-size:16px;font-weight:600}
.alert-card p{font-size:14px;line-height:1.5;margin-top:10px}
.alert-card .btn{height:34px;font-size:13px;margin-top:14px;padding:0 16px}

/* footer */
.footer{position:absolute;top:4080px;left:0;width:1200px;height:352px;background:var(--teal-dark);color:var(--white)}
.f-cols{display:flex;padding:40px 18px 0}
.f-brand{width:290px;padding-right:24px;font-size:13px;line-height:1.5}
.f-brand .mark{width:28px;height:28px;background:var(--white);border-radius:4px;margin-bottom:12px}
.f-col{width:300px;font-size:13px;line-height:1.5}
.f-col h4{font-family:"Playfair Display",serif;font-size:16px;margin-bottom:14px}
.f-col li{list-style:none;display:flex;align-items:center;gap:8px;margin-bottom:6px}
.f-col .icon{width:14px;height:14px}
.f-bottom{position:absolute;left:18px;right:18px;bottom:36px;border-top:1px solid rgba(255,255,255,.25);padding-top:24px;text-align:center;font-size:13px;color:#d8eeee}
</style>
</head>
<body>

<section class="hero">
  <div class="hero-photo" role="img" aria-label="Photo of a stainless commercial kitchen with cooking line"></div>
  <nav class="nav">
    <a>Services</a><a>About</a><a>Testimonials</a><a>Contact</a>
    <a class="btn btn-teal call"><svg class="icon" viewBox="0 0 24 24"><path d="M22 16.9v3a2 2 0 0 1-2.2 2 19.8 19.8 0 0 1-8.6-3.1 19.5 19.5 0 0 1-6-6A19.8 19.8 0 0 1 2.1 4.2 2 2 0 0 1 4.1 2h3a2 2 0 0 1 2 1.7c.1 1 .4 1.9.7 2.8a2 2 0 0 1-.5 2.1L8 9.9a16 16 0 0 0 6 6l1.3-1.3a2 2 0 0 1 2.1-.4c.9.3 1.8.6 2.8.7a2 2 0 0 1 1.7 2z"/></svg>Call Now</a>
  </nav>
  <div class="hero-copy">
    <h1>Professional Commercial<br>Kitchen Equipment Service</h1>
    <p>Expert repair, maintenance, and installation services for restaurants, cafes, and commercial kitchens. When your equipment breaks down, we get you back up and running fast.</p>
  </div>
  <div class="hero-actions">
    <a class="btn btn-white">Request Service</a>
    <span class="btn blank"></span>
  </div>
</section>

<section class="services">
  <h2>Our Expert Services</h2>
  <p class="lead">We specialize in commercial cooking equipment service for restaurants, cafes, and food service operations. Cooking equipment is our focus - pure kitchen equipment expertise.</p>
  <div class="svc-cards">
    <div class="svc-card"><div class="badge"><svg class="icon" viewBox="0 0 24 24"><path d="M14.7 6.3a4 4 0 0 0 5 5L21 13l-8 8-3-3 8-8-1.3-1.3a4 4 0 0 0-5-5zM3 21l6-6"/></svg></div><h3>Equipment Repair</h3><p>Fast, reliable repairs for all commercial cooking equipment including ovens, grills, fryers, and more.</p></div>
    <div class="svc-card"><div class="badge"><svg class="icon" viewBox="0 0 24 24"><circle cx="12" cy="12" r="9"/><path d="M12 7v5l3 2"/></svg></div><h3>Preventive Maintenance</h3><p>Regular maintenance programs to prevent breakdowns and extend equipment life.</p></div>
    <div class="svc-card"><div class="badge"><svg class="icon" viewBox="0 0 24 24"><path d="M12 3l8 3v6c0 5-3.5 8-8 9-4.5-1-8-4-8-9V6z"/></svg></div><h3>Safety Inspections</h3><p>Comprehensive safety inspections to ensure your equipment meets all regulatory standards.</p></div>
  </div>
  <div class="equip">
    <h3>Equipment We Service</h3>
    <ul>
      <li>Commercial Ovens</li><li>Grills &amp; Griddles</li><li>Deep Fryers</li><li>Range Tops</li>
      <li>Steamers</li><li>Broilers</li><li>Warming Equipment</li><li>Ventilation Hoods</li>
    </ul>
  </div>
</section>

<section class="trust">
  <div class="trust-copy">
    <h2>Why Restaurant Owners Trust Keystone</h2>
    <p>For over a decade, we've been the go-to service provider for commercial kitchens across the region. Our certified technicians understand the urgency of equipment failures in food service and respond with the speed and expertise you need.</p>
    <ul class="checks">
      <li><svg class="icon" viewBox="0 0 24 24"><circle cx="12" cy="12" r="9"/><path d="M8 12l3 3 5-6"/></svg>24/7 Emergency Service Available</li>
      <li><svg class="icon" viewBox="0 0 24 24"><circle cx="12" cy="12" r="9"/><path d="M8 12l3 3 5-6"/></svg>Licensed &amp; Certified Technicians</li>
      <li><svg class="icon" viewBox="0 0 24 24"><circle cx="12" cy="12" r="9"/><path d="M8 12l3 3 5-6"/></svg>All Major Equipment Brands</li>
      <li><svg class="icon" viewBox="0 0 24 24"><circle cx="12" cy="12" r="9"/><path d="M8 12l3 3 5-6"/></svg>Transparent Pricing</li>
      <li><svg class="icon" viewBox="0 0 24 24"><circle cx="12" cy="12" r="9"/><path d="M8 12l3 3 5-6"/></svg>Same-Day Service Available</li>
      <li><svg class="icon" viewBox="0 0 24 24"><circle cx="12" cy="12" r="9"/><path d="M8 12l3 3 5-6"/></svg>Parts &amp; Labor Warranty</li>
    </ul>
    <div class="trust-actions"><a class="btn btn-teal">Get Service Quote</a><a class="btn btn-outline">Call Now</a></div>
  </div>
  <div class="trust-photo" role="img" aria-label="Photo of a technician servicing a commercial range in a restaurant kitchen"></div>
  <div class="stats">
    <div class="stat"><svg class="icon" viewBox="0 0 24 24"><circle cx="9" cy="8" r="3"/><path d="M3 20c0-3 3-5 6-5s6 2 6 5M16 5a3 3 0 0 1 0 6M21 20c0-2.5-1.5-4.3-4-4.8"/></svg><strong>500+</strong><span>Restaurants Served</span></div>
    <div class="stat"><svg class="icon" viewBox="0 0 24 24"><circle cx="12" cy="12" r="9"/><path d="M12 7v5l3 2"/></svg><strong>&lt; 2hr</strong><span>Response Time</span></div>
  </div>
</section>

<section class="reviews">
  <h2>What Our Customers Say</h2>
  <p class="lead">Don't just take our word for it. Here's what restaurant owners and managers say about our service.</p>
  <div class="quotes">
    <div class="quote"><div class="stars">★★★★★</div><p>"Keystone saved our dinner rush. When our main oven went down during peak hours, they had a technician here within 45 minutes. Professional, fast, and reliable service."</p><div class="who"><strong>Dana Whitfield</strong><span>Restaurant Manager</span><br>Bistro on Main Street</div></div>
    <div class="quote"><div class="stars">★★★★★</div><p>"Their preventive maintenance program has kept our kitchen running smoothly for three years. No unexpected breakdowns, and their technicians really know commercial equipment."</p><div class="who"><strong>Owen Park</strong><span>Owner</span><br>Harbor Fusion Kitchen</div></div>
    <div class="quote"><div class="stars">★★★★★</div><p>"We use Keystone for all of our restaurant locations. They're responsive, professional, and their pricing is transparent. Highly recommend for any commercial kitchen."</p><div class="who"><strong>Laura Brennan</strong><span>Operations Director</span><br>Fresh Table Group</div></div>
    <div class="quote"><div class="stars">★★★★★</div><p>"Outstanding service! They diagnosed our fryer issues immediately and had the parts in stock. Our kitchen was back to full capacity the same day."</p><div class="who"><strong>Marco Ellison</strong><span>Kitchen Manager</span><br>Coastal Seafood House</div></div>
  </div>
  <div class="join">
    <h3>Join Our Satisfied Customers</h3>
    <p>Experience the same reliable, professional service that keeps kitchens running smoothly across the city.</p>
    <div class="row"><a class="btn btn-teal">Get Started Today</a><a class="btn btn-outline">Call Now: (555) 014-2390</a></div>
  </div>
</section>

<section class="emergency">
  <h2>Equipment Emergency? We're Here 24/7</h2>
  <p>When your kitchen equipment breaks down, every minute costs you money. Our emergency service team is standing by to get you back in business fast.</p>
  <div class="row">
    <a class="btn btn-white"><svg class="icon" viewBox="0 0 24 24"><path d="M22 16.9v3a2 2 0 0 1-2.2 2 19.8 19.8 0 0 1-8.6-3.1 19.5 19.5 0 0 1-6-6A19.8 19.8 0 0 1 2.1 4.2 2 2 0 0 1 4.1 2h3a2 2 0 0 1 2 1.7c.1 1 .4 1.9.7 2.8a2 2 0 0 1-.5 2.1L8 9.9a16 16 0 0 0 6 6l1.3-1.3a2 2 0 0 1 2.1-.4c.9.3 1.8.6 2.8.7a2 2 0 0 1 1.7 2z"/></svg>Call Emergency Line</a>
    <span class="btn btn-white"></span>
  </div>
</section>

<section class="request">
  <h2>Request Service</h2>
  <p class="lead">Get fast, reliable service for your commercial kitchen equipment. Contact us today.</p>
  <div class="form-card">
    <h3>Service Request Form</h3>
    <div class="grid">
      <div class="field"><label>Your Name *</label><div class="input">John Smith</div></div>
      <div class="field"><label>Email Address *</label><div class="input">john@example.com</div></div>
      <div class="field"><label>Phone Number *</label><div class="input">(555) 123-4567</div></div>
      <div class="field"><label>Equipment Type *</label><div class="input">e.g., Oven, Grill, Fryer</div></div>
      <div class="field full"><label>Service Details *</label><div class="input area">Describe the issue or service needed...</div></div>
    </div>
    <a class="btn btn-teal"><svg class="icon" viewBox="0 0 24 24"><path d="M22 2L11 13M22 2l-7 20-4-9-9-4z"/></svg>Request Service</a>
  </div>
  <div class="contact-card">
    <h3>Contact Information</h3>
    <div class="c-row"><div class="dot"><svg class="icon" viewBox="0 0 24 24"><path d="M22 16.9v3a2 2 0 0 1-2.2 2 19.8 19.8 0 0 1-8.6-3.1 19.5 19.5 0 0 1-6-6A19.8 19.8 0 0 1 2.1 4.2 2 2 0 0 1 4.1 2h3a2 2 0 0 1 2 1.7c.1 1 .4 1.9.7 2.8a2 2 0 0 1-.5 2.1L8 9.9a16 16 0 0 0 6 6l1.3-1.3a2 2 0 0 1 2.1-.4c.9.3 1.8.6 2.8.7a2 2 0 0 1 1.7 2z"/></svg></div><div><strong>Call Us Now</strong><span>(555) 014-2390</span></div></div>
    <div class="c-row"><div class="dot"><svg class="icon" viewBox="0 0 24 24"><rect x="3" y="5" width="18" height="14" rx="2"/><path d="M3 7l9 6 9-6"/></svg></div><div><strong>Email Us</strong><span>service@keystonekitchenservice.com</span></div></div>
  </div>
  <div class="alert-card">
    <h3>Emergency Service Available</h3>
    <p>Equipment breakdown? We provide 24/7 emergency service to get your kitchen running again.</p>
    <a class="btn btn-white">Call Emergency Line</a>
  </div>
</section>

<footer class="footer">
  <div class="f-cols">
    <div class="f-brand"><div class="mark"></div>Professional commercial kitchen equipment service for restaurants, cafes, and commercial kitchens. Expert repair, maintenance, and installation services.</div>
    <div class="f-col"><h4>Contact Info</h4><ul>
      <li><svg class="icon" viewBox="0 0 24 24"><path d="M22 16.9v3a2 2 0 0 1-2.2 2A19.8 19.8 0 0 1 2.1 4.2 2 2 0 0 1 4.1 2h3l2 5-2.5 2a16 16 0 0 0 7 7l2-2.5 5 2z"/></svg>(555) 014-2390</li>
      <li><svg class="icon" viewBox="0 0 24 24"><rect x="3" y="5" width="18" height="14" rx="2"/><path d="M3 7l9 6 9-6"/></svg>service@keystonekitchenservice.com</li>
      <li><svg class="icon" viewBox="0 0 24 24"><path d="M12 21s-7-6.5-7-12a7 7 0 0 1 14 0c0 5.5-7 12-7 12z"/><circle cx="12" cy="9" r="2.5"/></svg>48 Harbor Lane<br>Millbrook, ST 20415</li>
    </ul></div>
    <div class="f-col"><h4>Service Hours</h4><ul>
      <li><svg class="icon" viewBox="0 0 24 24"><circle cx="12" cy="12" r="9"/><path d="M12 7v5l3 2"/></svg>24/7 Emergency Service</li>
      <li>Mon-Fri: 7:00 AM - 6:00 PM</li><li>Sat: 8:00 AM - 4:00 PM</li><li>Sun: Emergency Calls Only</li>
    </ul></div>
    <div class="f-col" style="width:260px"><h4>Our Services</h4><ul>
      <li>Equipment Repair</li><li>Preventive Maintenance</li><li>Equipment Installation</li><li>Emergency Service</li><li>Safety Inspections</li><li>Parts Replacement</li>
    </ul></div>
  </div>
  <div class="f-bottom">© 2024 Keystone Kitchen Service. All rights reserved. | Professional Commercial Kitchen Equipment Service</div>
</footer>

</body>
</html>
```